BUSINESS CARD - HALLORAN FIELD SERVICES

I would like to create a business card for my fertilizer spreading business. I would like to incorporate my existing logo and also a description of the services offered. The business card will be given to farmers so must be kept simple but effective. It will also be left in stores so much also be eye catching in order to stand out from other cards.

Target Market(s)

FARMERS

Requirements
Must have
• FRONT OF CARD = EXISTING LOGO + "CUSTOMISED SPREADING" below the logo

REAR Of CARD = SERVICES OFFERED AND CONTACT DETAILS

- Bulk fertilizer including Lime, Gypsum, Manure & Compost
- Granular fertilizer including Single Super, Urea, Terragran, & Custom Blends
- Modern equipment - Autosteer & Variable Rate Capable
- Friendly & Reliable Service
- Contact Gus: 0471 592 318
Nice to have
• utilize same color scheme as existing logo

```html
<!DOCTYPE html>
<html lang="en">
<head>
<meta charset="utf-8">
<title>Halloran Field Services – Business Card</title>
<link rel="stylesheet" href="https://fonts.googleapis.com/css2?family=Open+Sans:wght@400;700&display=swap">
<style>
  :root {
    --page-bg: #e4e4e4;
    --card-bg: #f4f4f4;
    --ink-grey: #565656;
    --ink-dark: #2f2f2f;
    --accent-orange: #ef9229;
  }
  * { margin: 0; padding: 0; box-sizing: border-box; }
  html, body { width: 1200px; height: 960px; overflow: hidden; }
  body {
    background: var(--page-bg);
    font-family: "Open Sans", Arial, sans-serif;
    position: relative;
  }
  .card {
    position: absolute;
    left: 310px;
    width: 588px;
    height: 360px;
    background: var(--card-bg);
    overflow: hidden;
  }
  .card--front { top: 102px; }
  .card--back { top: 507px; }

  /* Front */
  .brand {
    position: absolute;
    left: 0; right: 0;
    top: 68px;
    display: flex;
    flex-direction: column;
    align-items: center;
  }
  .brand__dot {
    width: 150px; height: 150px;
    border-radius: 50%;
    background: var(--ink-grey);
    margin-bottom: 10px;
  }
  .brand__name {
    font-weight: 700;
    font-size: 36px;
    color: var(--ink-grey);
    letter-spacing: -0.5px;
    line-height: 1.1;
  }
  .tagline {
    position: absolute;
    left: 0; right: 0;
    top: 306px;
    text-align: center;
    font-weight: 700;
    font-size: 21px;
    letter-spacing: 1.6px;
    color: var(--ink-grey);
  }
  .tagline__accent { color: var(--accent-orange); }

  /* Back */
  .scene-area {
    position: absolute;
    left: 0; top: 0;
    width: 588px; height: 360px;
  }
  .contact {
    position: absolute;
    left: 46px;
    top: 104px;
  }
  .contact__name {
    font-weight: 700;
    font-size: 30px;
    color: var(--accent-orange);
    margin-left: 48px;
    line-height: 1.1;
  }
  .contact__phone {
    display: flex;
    align-items: center;
    gap: 4px;
    font-size: 21px;
    color: var(--ink-dark);
    line-height: 1.2;
  }
  .contact__phone svg { width: 20px; height: 20px; }

  .services {
    position: absolute;
    left: 304px;
    top: 48px;
    list-style: none;
  }
  .service { margin-bottom: 13px; }
  .service__title {
    display: flex;
    align-items: center;
    gap: 6px;
    font-weight: 700;
    font-size: 18.5px;
    color: var(--accent-orange);
    line-height: 22px;
  }
  .service__title svg { width: 14px; height: 14px; }
  .service__detail {
    padding-left: 20px;
    font-size: 18.5px;
    color: var(--ink-dark);
    line-height: 22px;
  }
</style>
</head>
<body>

<section class="card card--front">
  <div class="brand">
    <div class="brand__dot"></div>
    <div class="brand__name">Halloran Field Services</div>
  </div>
  <p class="tagline"><span class="tagline__accent">CUSTOMIZED</span> SPREADING</p>
</section>

<section class="card card--back">
  <svg class="scene-area" viewBox="0 0 588 360" role="img" aria-label="Illustration area: cattle and sheep standing on a grassy paddock under an arching wheat stem">
    <path d="M0 195 H255 V300 H588 V360 H0 Z" fill="var(--ink-grey)"/>
  </svg>

  <div class="contact">
    <p class="contact__name">Gus</p>
    <p class="contact__phone">
      <svg viewBox="0 0 24 24" aria-hidden="true">
        <circle cx="12" cy="12" r="10" fill="none" stroke="var(--accent-orange)" stroke-width="2"/>
        <path d="M8.5 6.8l1.6-.4 1.2 2.6-1.1 1a7 7 0 0 0 3.8 3.8l1-1.1 2.6 1.2-.4 1.6c-.2.7-.9 1.1-1.6 1A10 10 0 0 1 7.5 8.4c-.1-.7.3-1.4 1-1.6z" fill="var(--accent-orange)"/>
      </svg>
      0471 592 318
    </p>
  </div>

  <ul class="services">
    <li class="service">
      <p class="service__title"><svg viewBox="0 0 14 14" aria-hidden="true"><path d="M2 12C2 5 6 2 13 1c0 7-4 11-11 11z" fill="var(--accent-orange)"/></svg>BULK FERTILIZER</p>
      <p class="service__detail">Lime, Gypsum,<br>Manure &amp; Compost</p>
    </li>
    <li class="service">
      <p class="service__title"><svg viewBox="0 0 14 14" aria-hidden="true"><path d="M2 12C2 5 6 2 13 1c0 7-4 11-11 11z" fill="var(--accent-orange)"/></svg>GRANULAR FERTILISER</p>
      <p class="service__detail">Single Super, Urea,<br>Terragran &amp; Custom Blends</p>
    </li>
    <li class="service">
      <p class="service__title"><svg viewBox="0 0 14 14" aria-hidden="true"><path d="M2 12C2 5 6 2 13 1c0 7-4 11-11 11z" fill="var(--accent-orange)"/></svg>MODERN EQUIPMENT</p>
      <p class="service__detail">Auto Steer &amp; Variable<br>Rate Capable</p>
    </li>
  </ul>
</section>

</body>
</html>
```